Design für 3-Monatskalender
Zielgruppe
Hallo, wir benötigen ein Design bzw. fertige Druckdaten für einen 3 Monatskalender mit den Feiertagen aus DE, AT und CH.
Format ist DIN A6, der Kalender wird benötigt für das Jahr 2024 und 2025.
Aufgabenstellung
Format: DIN A6
Kalendarium 2024 und 2025
Feiertage aus DE, AT und CH
Beispiel anbei, wichtig ist, das wir einen Magnetischen Ring als Datumsschieber nehmen. Der Ring hat die Maße: Durchmesser = 12mm Innendruchmesser = 10mm

```html
<!DOCTYPE html>
<html lang="de">
<head>
<meta charset="utf-8">
<title>3-Monatskalender Dezember 2023 – Februar 2024</title>
<link rel="stylesheet" href="https://fonts.googleapis.com/css2?family=Barlow:wght@300;400;700&display=swap">
<style>
  :root {
    --backdrop: #ececec;
    --sheet: #ffffff;
    --ink: #1a1a1a;
    --sunday: #c0141c;
    --rule: #6a6a6a;
    --muted: #333333;
  }
  * { margin: 0; padding: 0; box-sizing: border-box; }
  html, body { width: 849px; height: 1200px; overflow: hidden; }
  body { background: var(--backdrop); font-family: "Barlow", Arial, sans-serif; color: var(--ink); position: relative; }

  .calendar-sheet {
    position: absolute; left: 71px; top: 76px; width: 384px; height: 558px;
    background: var(--sheet);
    box-shadow: 3px 4px 6px rgba(0,0,0,.25);
  }
  .month { position: absolute; left: 0; width: 384px; height: 178px; }
  .month--dec { top: 0; }
  .month--jan { top: 177px; }
  .month--feb { top: 355px; }

  .year { position: absolute; left: 19px; top: 33px; font-size: 11px; font-weight: 400; letter-spacing: .2px; }
  .month--jan .year { font-weight: 700; }

  .month-name {
    position: absolute; left: 44px; top: 181px;
    transform-origin: 0 0; transform: rotate(-90deg);
    font-size: 7.6px; white-space: nowrap; width: 122px; text-align: right;
  }
  .month--jan .month-name, .month--feb .month-name { width: 106px; text-align: right; }

  .rules {
    position: absolute; left: 52px; top: 35px; width: 283.5px; height: 146px;
    background: repeating-linear-gradient(to right, transparent 0 39.6px, var(--rule) 39.6px 40.5px);
  }
  .weekdays, .days {
    position: absolute; left: 52px; width: 283.5px;
    display: grid; grid-template-columns: repeat(7, 40.5px);
  }
  .weekdays { top: 34px; }
  .weekday { font-size: 4.4px; line-height: 5.2px; text-align: right; padding-right: 4px; color: var(--muted); }

  .days { top: 59px; grid-auto-rows: 25.7px; }
  .day {
    font-size: 18px; font-weight: 300; line-height: 25.7px;
    text-align: right; padding-right: 4.5px; position: relative;
  }
  .month--jan .day { font-weight: 700; }
  .day.sun { color: var(--sunday); }
  .month--dec .day.sun { font-weight: 300; }

  .holiday { position: absolute; top: 6px; display: flex; flex-direction: column; gap: .5px; }
  .holiday i {
    display: block; width: 5.4px; height: 5.4px; border: .6px solid var(--sunday); border-radius: 50%;
    font-style: normal; font-size: 2.8px; line-height: 4.4px; text-align: center; color: var(--sunday); font-weight: 400;
  }
  .day--2 .holiday { right: 22px; }
  .day--1 .holiday { right: 16px; top: 9px; }

  .week-label { position: absolute; left: 349px; top: 42px; font-size: 4.6px; width: 20px; text-align: center; }
  .weeks { position: absolute; left: 349px; top: 59px; width: 20px; display: grid; grid-auto-rows: 25.7px; }
  .week { font-size: 8.5px; line-height: 27px; text-align: center; }
</style>
</head>
<body>
<main class="calendar-sheet" aria-label="3-Monatskalender">

  <section class="month month--dec">
    <div class="year">2023</div>
    <div class="month-name">Dezember | December | Décembre</div>
    <div class="rules"></div>
    <div class="weekdays">
      <div class="weekday">Montag<br>Monday<br>Lundi</div>
      <div class="weekday">Dienstag<br>Tuesday<br>Mardi</div>
      <div class="weekday">Mittwoch<br>Wednesday<br>Mercredi</div>
      <div class="weekday">Donnerstag<br>Thursday<br>Jeudi</div>
      <div class="weekday">Freitag<br>Friday<br>Vendreday</div>
      <div class="weekday">Samstag<br>Saturday<br>Samedi</div>
      <div class="weekday">Sonntag<br>Sunday<br>Dimanche</div>
    </div>
    <div class="days">
      <div class="day" style="grid-column-start:5">1</div><div class="day">2</div><div class="day sun">3</div>
      <div class="day">4</div><div class="day">5</div><div class="day">6</div><div class="day">7</div>
      <div class="day day--1"><span class="holiday"><i>A</i><i>CH</i></span>8</div><div class="day">9</div><div class="day sun">10</div>
      <div class="day">11</div><div class="day">12</div><div class="day">13</div><div class="day">14</div><div class="day">15</div><div class="day">16</div><div class="day sun">17</div>
      <div class="day">18</div><div class="day">19</div><div class="day">20</div><div class="day">21</div><div class="day">22</div><div class="day">23</div><div class="day sun">24</div>
      <div class="day day--2"><span class="holiday"><i>D</i><i>A</i><i>CH</i></span>25</div>
      <div class="day day--2"><span class="holiday"><i>D</i><i>A</i><i>CH</i></span>26</div>
      <div class="day">27</div><div class="day">28</div><div class="day">29</div><div class="day">30</div><div class="day sun">31</div>
    </div>
    <div class="week-label">KW</div>
    <div class="weeks"><div class="week">48</div><div class="week">49</div><div class="week">50</div><div class="week">51</div><div class="week">52</div></div>
  </section>

  <section class="month month--jan">
    <div class="year">2024</div>
    <div class="month-name">Januar | January | Janvier</div>
    <div class="rules"></div>
    <div class="weekdays">
      <div class="weekday">Montag<br>Monday<br>Lundi</div>
      <div class="weekday">Dienstag<br>Tuesday<br>Mardi</div>
      <div class="weekday">Mittwoch<br>Wednesday<br>Mercredi</div>
      <div class="weekday">Donnerstag<br>Thursday<br>Jeudi</div>
      <div class="weekday">Freitag<br>Friday<br>Vendreday</div>
      <div class="weekday">Samstag<br>Saturday<br>Samedi</div>
      <div class="weekday">Sonntag<br>Sunday<br>Dimanche</div>
    </div>
    <div class="days">
      <div class="day day--1"><span class="holiday" style="right:13px;top:3px"><i>D</i><i>A</i><i>CH</i></span>1</div>
      <div class="day">2</div><div class="day">3</div><div class="day">4</div><div class="day">5</div>
      <div class="day day--1"><span class="holiday"><i>A</i><i>CH</i></span>6</div><div class="day sun">7</div>
      <div class="day">8</div><div class="day">9</div><div class="day">10</div><div class="day">11</div><div class="day">12</div><div class="day">13</div><div class="day sun">14</div>
      <div class="day">15</div><div class="day">16</div><div class="day">17</div><div class="day">18</div><div class="day">19</div><div class="day">20</div><div class="day sun">21</div>
      <div class="day">22</div><div class="day">23</div><div class="day">24</div><div class="day">25</div><div class="day">26</div><div class="day">27</div><div class="day sun">28</div>
      <div class="day">29</div><div class="day">30</div><div class="day">31</div>
    </div>
    <div class="week-label">KW</div>
    <div class="weeks"><div class="week">1</div><div class="week">2</div><div class="week">3</div><div class="week">4</div><div class="week">5</div></div>
  </section>

  <section class="month month--feb">
    <div class="year">2024</div>
    <div class="month-name">Februar | February | Février</div>
    <div class="rules"></div>
    <div class="weekdays">
      <div class="weekday">Montag<br>Monday<br>Lundi</div>
      <div class="weekday">Dienstag<br>Tuesday<br>Mardi</div>
      <div class="weekday">Mittwoch<br>Wednesday<br>Mercredi</div>
      <div class="weekday">Donnerstag<br>Thursday<br>Jeudi</div>
      <div class="weekday">Freitag<br>Friday<br>Vendreday</div>
      <div class="weekday">Samstag<br>Saturday<br>Samedi</div>
      <div class="weekday">Sonntag<br>Sunday<br>Dimanche</div>
    </div>
    <div class="days">
      <div class="day" style="grid-column-start:4">1</div><div class="day">2</div><div class="day">3</div><div class="day sun">4</div>
      <div class="day">5</div><div class="day">6</div><div class="day">7</div><div class="day">8</div><div class="day">9</div><div class="day">10</div><div class="day sun">11</div>
      <div class="day">12</div><div class="day">13</div><div class="day">14</div><div class="day">15</div><div class="day">16</div><div class="day">17</div><div class="day sun">18</div>
      <div class="day">19</div><div class="day">20</div><div class="day">21</div><div class="day">22</div><div class="day">23</div><div class="day">24</div><div class="day sun">25</div>
      <div class="day">26</div><div class="day">27</div><div class="day">28</div><div class="day">29</div>
    </div>
    <div class="week-label">KW</div>
    <div class="weeks"><div class="week">5</div><div class="week">6</div><div class="week">7</div><div class="week">8</div><div class="week">9</div></div>
  </section>

</main>
</body>
</html>
```